brochure desing for agriculture and amenity company

create a booklet showcasing what services our company can offer. Draw design inspiration from the attached buisness card and also from the website www.brindlefieldgrounds.co.uk. the leaflet should focus on cut and clear, banks mowing/flailing reseeding and site clearance as the primary services being showcased. A5 page size, bifold

```html
<!DOCTYPE html>
<html lang="en">
<head>
<meta charset="utf-8">
<title>Brindlefield Grounds – Services Brochure Spread</title>
<link rel="stylesheet" href="https://fonts.googleapis.com/css2?family=Michroma&family=Poppins:wght@300;400&display=swap">
<style>
  :root {
    --bg: #dcdcdc;
    --paper: #ffffff;
    --band: #ebebeb;
    --ink: #1e1e1e;
    --body: #4a4a4a;
    --green: #2f9a1f;
    --green-bright: #3cb52a;
    --sky: #8fb8e0;
    --grass: #5f8a3a;
    --soil: #8a6a4a;
  }
  * { box-sizing: border-box; margin: 0; padding: 0; }
  html, body { width: 1200px; height: 900px; overflow: hidden; background: var(--bg); }
  .spread {
    position: absolute; left: 60px; top: 68px;
    width: 1080px; height: 764px;
    display: flex;
    box-shadow: 0 18px 40px rgba(0,0,0,0.18);
  }
  .page { position: relative; width: 540px; height: 764px; background: var(--paper); overflow: hidden; }
  .page--left { border-right: 1px solid #e4e4e4; }

  .service-title {
    position: absolute; display: flex; align-items: center; gap: 10px;
    font-family: "Michroma", sans-serif; font-size: 14px; letter-spacing: 0.5px;
    color: var(--ink); text-transform: uppercase; white-space: nowrap;
  }
  .service-title::before {
    content: ""; width: 18px; height: 15px; background: var(--green); flex: none;
  }
  .service-title .subtitle { color: var(--green-bright); font-size: 8px; margin-left: 4px; }

  .service-copy {
    position: absolute;
    font-family: "Poppins", sans-serif; font-weight: 300;
    font-size: 9.5px; line-height: 1.6; color: var(--body);
  }
  .service-copy p + p { margin-top: 8px; }

  .photo-strip { position: absolute; background: var(--green); }
  .photo { position: absolute; inset: 0; }
  .photo--field { background: linear-gradient(180deg, var(--sky) 0%, #b9d0e6 38%, var(--grass) 62%, #4b6d2e 100%); }
  .photo--soil { background: linear-gradient(180deg, #a7c2dc 0%, #7c9a5c 30%, var(--soil) 55%, #6f5239 100%); }
  .photo--hedge { background: linear-gradient(160deg, #4d6e34 0%, #7a9a4c 45%, #9b7b56 100%); }
  .photo--frost { background: linear-gradient(180deg, #d5c2a6 0%, #a9b2a4 40%, #8d9a86 100%); }
  .photo--slope { background: linear-gradient(180deg, #b9cbe0 0%, #6f9b3e 40%, #4f7a2a 100%); }

  .photo-circle {
    position: absolute; width: 92px; height: 92px; border-radius: 50%;
    border: 3px solid var(--green); box-shadow: 0 0 0 4px var(--paper);
  }

  .band { position: absolute; left: 0; right: 0; background: var(--band); }

  .extra-services {
    position: absolute; list-style: none;
    font-family: "Poppins", sans-serif; font-weight: 300; font-size: 10px;
    line-height: 1.7; color: var(--body);
  }
  .extra-services li::before { content: "•"; color: var(--green); margin-right: 5px; }

  .site-url {
    position: absolute; left: 0; right: 0; text-align: center;
    font-family: "Poppins", sans-serif; font-size: 7.5px; letter-spacing: 4px;
    color: #555; text-transform: uppercase;
  }
</style>
</head>
<body>
<main class="spread">

  <section class="page page--left">
    <h2 class="service-title" style="left:48px; top:60px;">Cut and Clear</h2>
    <div class="service-copy" style="left:70px; top:90px; width:410px;">
      <p>Our most popular and thorough service, cut and clear is ideal for areas of grassland in environmental stewardship. The grass is mown, raked and baled, with the bales being brought back and composted on farm by ourselves. This is ideal for larger areas of grass. All of this cut material removed allows the wildflowers to flourish (simulating a summer hay cut).</p>
    </div>
    <div class="photo-strip" style="left:0; top:182px; width:540px; height:120px;">
      <div class="photo photo--field" role="img" aria-label="Tractor mowing a grass field under a blue sky" style="clip-path:polygon(0 0,46% 0,52% 100%,0 100%);"></div>
      <div class="photo photo--hedge" role="img" aria-label="Tractors with trailer collecting cut grass beside trees" style="clip-path:polygon(47% 0,66% 0,72% 100%,53% 100%);"></div>
      <div class="photo photo--soil" role="img" aria-label="Tractor baling cut material on a cleared field" style="clip-path:polygon(67% 0,100% 0,100% 100%,73% 100%);"></div>
    </div>

    <h2 class="service-title" style="left:48px; top:330px;">Banks Mowing/Flailing</h2>
    <div class="service-copy" style="left:70px; top:360px; width:420px;">
      <p>We operate several Kestrel tractors which are purpose made for working on steep slopes. These are equipped with either mulchers or grass flails depending on the client's needs. These machines are equipped with wide flotation tyres ensuring they do not damage lines and can handle wet and marshy areas.</p>
      <p>The flail collector is a cross between flailing and cut and clear. Perfect for a high-quality finish on smaller areas with no mulch left behind. All of the collected cuttings are taken away and disposed of by ourselves. This machine is perfect for areas with short and medium length material and thanks to the use of flotation tyres is suitable for use on more sensitive areas.</p>
    </div>
    <div class="photo-strip" style="left:0; top:545px; width:540px; height:150px;">
      <div class="photo photo--slope" role="img" aria-label="Slope tractor mowing a grass bank" style="clip-path:polygon(0 0,28% 0,34% 100%,0 100%);"></div>
      <div class="photo photo--hedge" role="img" aria-label="Compact tractor flailing along a hedge line" style="clip-path:polygon(29% 0,50% 0,56% 100%,35% 100%);"></div>
      <div class="photo photo--frost" role="img" aria-label="Tractor with flail collector on a frosty bank at sunrise" style="clip-path:polygon(51% 0,100% 0,100% 100%,57% 100%);"></div>
    </div>
    <p class="site-url" style="top:726px;">www.brindlefieldgrounds.co.uk</p>
  </section>

  <section class="page page--right">
    <h2 class="service-title" style="left:48px; top:150px;">Reseeding</h2>
    <div class="service-copy" style="left:70px; top:178px; width:420px;">
      <p>The objective of grass reinstatement is to restore the area to its original condition, provide erosion control and enhance the aesthetic appearance. To achieve the best results, we first rotovate the area to create a fine tilth and then power harrow, to ensure it is level. On areas where groundworks may have taken place resulting in small stones/rubble we also offer stone burying to improve the structure and bury any unwanted residue. We can supply wildflower seed mixes to suit all requirements.</p>
    </div>
    <div class="photo-strip" style="left:0; top:272px; width:540px; height:130px;">
      <div class="photo photo--field" role="img" aria-label="Tractor preparing ground for reseeding beside houses" style="clip-path:polygon(0 0,44% 0,50% 100%,0 100%);"></div>
      <div class="photo photo--soil" role="img" aria-label="Freshly harrowed soil ready for seed" style="clip-path:polygon(45% 0,72% 0,78% 100%,51% 100%);"></div>
      <div class="photo photo--slope" role="img" aria-label="Workers raking a seeded area next to a tractor" style="clip-path:polygon(73% 0,100% 0,100% 100%,79% 100%);"></div>
    </div>

    <div class="band" style="top:402px; height:250px;"></div>
    <h2 class="service-title" style="left:48px; top:432px;">Site Clearance <span class="subtitle">/ Other Services</span></h2>
    <div class="service-copy" style="left:70px; top:460px; width:260px;">
      <p>Perfect for areas of ground that have become overgrown either with brambles or self-set trees. We can offer a variety of mulching flails for lighter materials such as brambles and smaller diameter trees.</p>
    </div>
    <div class="photo-circle photo--soil" role="img" aria-label="Tractor with seed drill on a cleared field" style="left:330px; top:452px;"></div>
    <div class="photo-circle photo--field" role="img" aria-label="Tractor topping a dry grass field" style="left:436px; top:418px;"></div>

    <ul class="extra-services" style="left:72px; top:572px;">
      <li>Grass topping for large areas</li>
      <li>Strimming/Brush cutting</li>
      <li>Direct drilling</li>
      <li>Fertilizer spreading</li>
      <li>Combining</li>
    </ul>

    <div class="photo-strip" style="left:200px; top:560px; width:340px; height:140px; clip-path:polygon(18% 0,100% 0,100% 100%,0 100%);">
      <div class="photo photo--hedge" role="img" aria-label="Mulching machine clearing an overgrown track" style="clip-path:polygon(18% 0,36% 0,42% 100%,0 100%);"></div>
      <div class="photo photo--frost" role="img" aria-label="Cleared frosty path between trees" style="clip-path:polygon(37% 0,60% 0,66% 100%,43% 100%);"></div>
      <div class="photo photo--hedge" role="img" aria-label="Tracked mulcher clearing dense brambles" style="clip-path:polygon(61% 0,100% 0,100% 100%,67% 100%);"></div>
    </div>
    <p class="site-url" style="top:726px;">www.brindlefieldgrounds.co.uk</p>
  </section>

</main>
</body>
</html>
```